Creative Businesss Card desgin!

Create a business card for our business Gleam window cleaning!
We are open to creative ideas as long as it maintains a professional image.

Target Market(s)

Small Commercial window cleaning clients including car dealerships, strata manager, cafe

Industry/Entity Type

Window Cleaning

Contact Information for Business Card

Daniel Prescott
General Manager
Gleam Window Cleaning

daniel@gleamservices.com.au
pane-care-southbank.com.au
Ph: 1800 GET GLEAM
Mob: 0437 582 061

Colors
fbed22
0392cd

Requirements
Should not have
• Stock window cleaning/ squeegee graphics

```html
<!DOCTYPE html>
<html lang="en">
<head>
<meta charset="utf-8">
<title>Gleam Window Cleaning – Business Card</title>
<link href="https://fonts.googleapis.com/css2?family=Montserrat:wght@300;700;800&family=Open+Sans:wght@400;600&display=swap" rel="stylesheet">
<style>
  :root {
    --brand-blue: #0f578e;
    --brand-yellow: #f2ea22;
    --paper: #ffffff;
    --ink: #2b2b2b;
    --backdrop: #e9ebee;
  }
  * { margin: 0; padding: 0; box-sizing: border-box; }
  html, body { width: 1200px; height: 1200px; overflow: hidden; }
  body {
    background: var(--backdrop);
    position: relative;
    font-family: "Open Sans", sans-serif;
  }
  .card {
    position: absolute;
    width: 600px;
    height: 366px;
    border-radius: 4px;
    overflow: hidden;
    box-shadow: 0 10px 30px rgba(0,0,0,0.18);
  }
  /* ---------- Back side ---------- */
  .card--back {
    top: 120px;
    left: 520px;
    background: var(--brand-blue);
    display: flex;
    align-items: center;
    justify-content: center;
  }
  .wordmark {
    color: var(--brand-yellow);
    font-family: "Montserrat", sans-serif;
    font-weight: 800;
    text-transform: uppercase;
    line-height: 1;
  }
  .card--back .wordmark__name { font-size: 84px; letter-spacing: 4px; display: block; }
  .card--back .wordmark__tagline { font-size: 26px; letter-spacing: 1.5px; display: block; margin-top: 6px; }

  /* ---------- Front side ---------- */
  .card--front {
    top: 660px;
    left: 80px;
    background: var(--paper);
  }
  .card__shapes { position: absolute; inset: 0; }
  .identity {
    position: absolute;
    top: 36px;
    left: 44px;
    color: var(--brand-blue);
    font-family: "Montserrat", sans-serif;
  }
  .identity__name { font-size: 38px; line-height: 1; text-transform: uppercase; letter-spacing: 0.5px; }
  .identity__first { font-weight: 800; }
  .identity__last { font-weight: 300; }
  .identity__title {
    font-family: "Open Sans", sans-serif;
    color: var(--ink);
    font-size: 18px;
    margin-top: 6px;
  }
  .identity__rule {
    width: 76px;
    height: 5px;
    background: var(--brand-blue);
    margin-top: 8px;
  }
  .contact {
    position: absolute;
    top: 145px;
    left: 44px;
    list-style: none;
    color: var(--ink);
    font-size: 16px;
    line-height: 1.6;
  }
  .contact__item { display: flex; align-items: center; gap: 10px; }
  .contact__item--strong { font-weight: 600; }
  .contact__icon { width: 15px; height: 15px; fill: var(--brand-blue); flex: none; }
  .card--front .wordmark {
    position: absolute;
    right: 28px;
    bottom: 26px;
    text-align: left;
  }
  .card--front .wordmark__name { font-size: 44px; letter-spacing: 2px; display: block; }
  .card--front .wordmark__tagline { font-size: 13px; letter-spacing: 0.8px; display: block; margin-top: 4px; }
</style>
</head>
<body>

  <section class="card card--back" aria-label="Business card, back">
    <div class="wordmark">
      <span class="wordmark__name">Gleam</span>
      <span class="wordmark__tagline">Window Cleaning</span>
    </div>
  </section>

  <section class="card card--front" aria-label="Business card, front">
    <svg class="card__shapes" viewBox="0 0 600 366" preserveAspectRatio="none" aria-hidden="true">
      <polygon points="150,366 600,80 600,110 230,366" fill="var(--brand-yellow)"/>
      <polygon points="230,366 600,110 600,366" fill="var(--brand-blue)"/>
    </svg>

    <div class="identity">
      <h1 class="identity__name"><span class="identity__first">Daniel</span> <span class="identity__last">Prescott</span></h1>
      <p class="identity__title">General Manager</p>
      <div class="identity__rule"></div>
    </div>

    <ul class="contact">
      <li class="contact__item contact__item--strong">
        <svg class="contact__icon" viewBox="0 0 16 16"><path d="M4 0h8a1 1 0 0 1 1 1v14a1 1 0 0 1-1 1H4a1 1 0 0 1-1-1V1a1 1 0 0 1 1-1zm1 2v10h6V2zm3 11a1 1 0 1 0 0 2 1 1 0 0 0 0-2z"/></svg>
        0437 582 061
      </li>
      <li class="contact__item">
        <svg class="contact__icon" viewBox="0 0 16 16"><path d="M3.6 1.2l2.3 2.6-1.3 1.7a10 10 0 0 0 5.9 5.9l1.7-1.3 2.6 2.3-1.4 2.3C7.7 14.5 1.5 8.3 1.3 2.6z"/></svg>
        1800 GET GLEAM
      </li>
      <li class="contact__item">
        <svg class="contact__icon" viewBox="0 0 16 16"><path d="M1 3h14v10H1zm1.5 1.3V5l5.5 3.6L13.5 5v-.7L8 7.8z"/></svg>
        daniel@gleamservices.com.au
      </li>
      <li class="contact__item">
        <svg class="contact__icon" viewBox="0 0 16 16"><circle cx="8" cy="8" r="7" fill="none" stroke="var(--brand-blue)" stroke-width="1.6"/><path d="M1 8h14M8 1c-3 3.5-3 10.5 0 14M8 1c3 3.5 3 10.5 0 14" fill="none" stroke="var(--brand-blue)" stroke-width="1.3"/></svg>
        pane-care-southbank.com.au
      </li>
    </ul>

    <div class="wordmark">
      <span class="wordmark__name">Gleam</span>
      <span class="wordmark__tagline">Window Cleaning</span>
    </div>
  </section>

</body>
</html>
```